Car Advertisement Design. 2090mm (H) x 4730mm(W)

Need a car exterior design for the kitchen company. Size is 2090mm (H) x 4730mm(W)

Target Market(s)

30-50 years

Requirements
Must have
• company logo and pics

```html
<!DOCTYPE html>
<html lang="en">
<head>
<meta charset="utf-8">
<title>Hearthline Interiors Co. – Vehicle Wrap Panel</title>
<link rel="stylesheet" href="https://fonts.googleapis.com/css2?family=Questrial&display=swap">
<style>
  :root {
    --brand-blue-deep: #1b4aa6;
    --brand-blue: #1a6fc0;
    --brand-blue-light: #2a8fd6;
    --brand-green: #3fae3a;
    --brand-green-light: #6cc04a;
    --paper: #ffffff;
    --stage: #ffffff;
    --wood-dark: #7a4a2a;
    --wood: #a8703f;
    --tile: #eef0f1;
  }
  * { margin: 0; padding: 0; box-sizing: border-box; }
  html, body {
    width: 1146px;
    height: 1200px;
    overflow: hidden;
    background: var(--stage);
  }
  .canvas {
    position: relative;
    width: 1146px;
    height: 1200px;
  }
  .wrap-panel {
    position: absolute;
    left: 30px;
    top: 359px;
    width: 1086px;
    height: 482px;
    box-shadow: 4px 5px 8px rgba(0,0,0,0.35);
  }
  .wrap-panel svg { display: block; width: 100%; height: 100%; }
  .brand-name, .brand-sub, .contact {
    font-family: "Questrial", "Century Gothic", sans-serif;
    fill: var(--paper);
  }
  .brand-name { font-size: 60px; letter-spacing: -1px; }
  .brand-sub { font-size: 12px; letter-spacing: 2px; }
  .contact-phone { font-size: 30px; }
  .contact-line { font-size: 20px; }
</style>
</head>
<body>
<main class="canvas">
  <section class="wrap-panel" aria-label="Hearthline Interiors Co. vehicle side panel">
    <svg viewBox="0 0 1285 570" xmlns="http://www.w3.org/2000/svg">
      <defs>
        <linearGradient id="blueField" x1="0" y1="0" x2="1" y2="0">
          <stop offset="0" stop-color="var(--brand-blue-deep)"/>
          <stop offset="1" stop-color="var(--brand-blue-light)"/>
        </linearGradient>
        <linearGradient id="kitchenLeft" x1="0" y1="0" x2="0" y2="1">
          <stop offset="0" stop-color="#a86a3c"/>
          <stop offset="0.18" stop-color="#f2f3f4"/>
          <stop offset="0.55" stop-color="#e9ebec"/>
          <stop offset="0.62" stop-color="#9a6238"/>
          <stop offset="0.85" stop-color="#8a5530"/>
          <stop offset="1" stop-color="#ddd8d2"/>
        </linearGradient>
        <linearGradient id="kitchenRight" x1="0" y1="0" x2="1" y2="1">
          <stop offset="0" stop-color="#f4f4f4"/>
          <stop offset="0.35" stop-color="#b07a4c"/>
          <stop offset="0.6" stop-color="#8e5a34"/>
          <stop offset="0.8" stop-color="#efefef"/>
          <stop offset="1" stop-color="#c9a27c"/>
        </linearGradient>
        <linearGradient id="tileBlue" x1="0" y1="0" x2="1" y2="1">
          <stop offset="0" stop-color="var(--brand-blue-light)"/>
          <stop offset="1" stop-color="var(--brand-blue-deep)"/>
        </linearGradient>
        <linearGradient id="tileGreen" x1="0" y1="0" x2="1" y2="1">
          <stop offset="0" stop-color="var(--brand-green-light)"/>
          <stop offset="1" stop-color="var(--brand-green)"/>
        </linearGradient>
      </defs>

      <!-- base -->
      <rect class="panel-base" width="1285" height="570" fill="var(--paper)"/>

      <!-- right kitchen area -->
      <g class="feature-right">
        <rect x="1380" y="80" width="700" height="700" rx="34" transform="rotate(45 885 80) translate(-495 -350)"
              fill="url(#kitchenRight)" role="img" aria-label="Photo area: modern kitchen with walnut wall cabinets, built-in ovens, white island and pendant lights"/>
        <rect x="885" y="-270" width="700" height="700" rx="34" transform="rotate(45 885 80)"
              fill="none" stroke="var(--brand-blue)" stroke-width="1.5"/>
      </g>

      <!-- blue field -->
      <polygon class="blue-field" points="0,0 700,0 405,295 680,570 0,570" fill="url(#blueField)"/>

      <!-- main kitchen diamond -->
      <g class="feature-main">
        <rect x="494" y="59" width="432" height="432" rx="32" transform="rotate(45 710 275)"
              fill="none" stroke="var(--brand-blue)" stroke-width="1.5" transform-origin="710 275"
              style="transform: rotate(45deg) scale(1.07);"/>
        <rect x="494" y="59" width="432" height="432" rx="30" transform="rotate(45 710 275)"
              fill="url(#kitchenLeft)" stroke="var(--paper)" stroke-width="14"
              role="img" aria-label="Photo area: kitchen with stainless range hood, white backsplash and walnut base cabinets"/>
      </g>

      <!-- accent tiles -->
      <rect class="tile-blue" x="968" y="338" width="184" height="184" rx="16" transform="rotate(45 1060 430)" fill="url(#tileBlue)"/>
      <rect class="tile-green" x="864" y="474" width="92" height="92" rx="10" transform="rotate(45 910 520)" fill="url(#tileGreen)"/>

      <!-- brand block -->
      <g class="brand">
        <rect class="brand-square" x="150" y="140" width="170" height="170" rx="6" fill="none" stroke="var(--paper)" stroke-width="10"/>
        <text class="brand-name" x="58" y="385">Hearthline</text>
        <text class="brand-sub" x="300" y="404">Interiors Co.</text>
      </g>

      <!-- contact -->
      <g class="contact">
        <text class="contact-phone" x="58" y="450">555.214.0670</text>
        <text class="contact-line" x="58" y="479">www.hearthlineinteriors.ca</text>
        <text class="contact-line" x="58" y="507">214 Cedar Row NE Brookfield, Alberta, T0A 0A0</text>
      </g>
    </svg>
  </section>
</main>
</body>
</html>
```